Business card design needed

I need a business card for my new Food & Lifestyle Coaching business - "Bloomvale Food & Lifestlye Coaching"

i already have a logo and would like to have that incorporated into the business card, obviously.

i would like a design that says "fresh" and "funky" - my target market is female, aged 20-45 so i want something that will stand out to them when they see it.

My "Company Colour" is Apple Green
Updates

Thankyou to everyone who has submitted a design for my project. At this stage i have quite a large number of designs to chose from and with only a short time until my project closes i am focusing now on chosing from those i have already shortlisted so am unfortunately not considering any new desings.

Thankyou again for your interest in my project.

Target Market(s)

Female, Health Conscious (or looking to improve their health/lifestyle), aged between 20-45

Industry/Entity Type

Business

Contact Information for Business Card

Tamsin Corley
Ph: 0417382946
Email: eatwell@marovex.com

Requirements
Must have
• Must include my existing Logo
Nice to have
• Would be nice to incoirporate and appointment card on the back

```html
<!DOCTYPE html>
<html lang="en">
<head>
<meta charset="utf-8">
<title>Bloomvale Food &amp; Lifestlye Coaching – Business &amp; Appointment Card</title>
<link href="https://fonts.googleapis.com/css2?family=Playfair+Display:ital,wght@0,700;1,700&family=Open+Sans:wght@400&display=swap" rel="stylesheet">
<style>
  :root {
    --apple-green: #8dc63f;
    --lime-edge: #bcd631;
    --card-white: #ffffff;
    --ink: #1e1e1e;
    --page-bg: #ecebe6;
    --rule: #ffffff;
  }
  * { box-sizing: border-box; margin: 0; padding: 0; }
  html, body {
    width: 1200px; height: 1000px; overflow: hidden;
    background: var(--page-bg);
  }
  .stage {
    position: relative; width: 1200px; height: 1000px;
  }
  .card {
    position: absolute; top: 160px;
    width: 380px; height: 680px;
    border-radius: 26px; overflow: hidden;
    box-shadow: 0 6px 18px rgba(0,0,0,0.18);
  }
  .card--front { left: 170px; background: var(--card-white); }
  .card--back  { left: 650px; background: var(--apple-green); color: var(--card-white); }

  .front-wave { position: absolute; left: 0; top: 0; width: 380px; height: 680px; }

  .wordmark {
    position: absolute; left: 0; width: 100%;
    display: flex; flex-direction: column; align-items: center;
    font-family: "Playfair Display", serif; font-weight: 700;
  }
  .wordmark__row { display: flex; align-items: center; gap: 10px; }
  .wordmark__dot {
    width: 26px; height: 26px; border-radius: 50%;
    background: var(--apple-green);
  }
  .wordmark__name { font-size: 44px; line-height: 1; }
  .wordmark__tagline { font-size: 13px; margin-top: 6px; letter-spacing: 0.2px; }
  .card--front .wordmark { top: 128px; color: var(--ink); }
  .card--back .wordmark { top: 212px; color: var(--card-white); }
  .card--back .wordmark__dot { background: var(--card-white); }

  .holder-name {
    position: absolute; top: 432px; width: 100%; text-align: center;
    font-family: "Playfair Display", serif; font-style: italic; font-weight: 700;
    font-size: 29px; color: var(--card-white); letter-spacing: 0.5px;
  }
  .contact {
    position: absolute; top: 538px; width: 100%; text-align: center;
    font-family: "Playfair Display", serif; font-weight: 700;
    font-size: 15px; color: var(--card-white); line-height: 30px; letter-spacing: 0.3px;
  }

  .reminder {
    position: absolute; width: 100%; text-align: center;
    font-family: "Playfair Display", serif; font-style: italic; font-weight: 700;
    font-size: 24px;
  }
  .reminder--title { top: 128px; }
  .reminder--label { top: 346px; letter-spacing: 0.5px; }

  .appt-field {
    position: absolute; left: 52px; right: 52px;
    display: flex; align-items: flex-end; gap: 8px;
    font-family: "Playfair Display", serif; font-style: italic; font-weight: 700;
    font-size: 19px;
  }
  .appt-field--date { top: 446px; }
  .appt-field--time { top: 516px; padding-left: 34px; }
  .appt-field__line {
    flex: 1; height: 0; border-bottom: 1.5px solid var(--rule); margin-bottom: 5px;
  }
</style>
</head>
<body>
<main class="stage">

  <section class="card card--front" aria-label="Business card front">
    <svg class="front-wave" viewBox="0 0 380 680" aria-hidden="true">
      <path d="M0 322 C 90 300, 180 340, 270 352 C 320 358, 355 354, 380 344 L380 680 L0 680 Z" fill="var(--lime-edge)"/>
      <path d="M0 334 C 90 312, 180 352, 270 364 C 320 370, 355 366, 380 356 L380 680 L0 680 Z" fill="var(--apple-green)"/>
    </svg>

    <div class="wordmark">
      <div class="wordmark__row">
        <span class="wordmark__dot"></span>
        <span class="wordmark__name">Bloomvale</span>
      </div>
      <span class="wordmark__tagline">Food &amp; Lifestlye Coaching</span>
    </div>

    <h1 class="holder-name">Tamsin Corley</h1>
    <p class="contact">
      0417382946<br>
      eatwell@marovex.com
    </p>
  </section>

  <section class="card card--back" aria-label="Appointment card back">
    <p class="reminder reminder--title">Don’t forget!</p>

    <div class="wordmark">
      <div class="wordmark__row">
        <span class="wordmark__dot"></span>
        <span class="wordmark__name">Bloomvale</span>
      </div>
      <span class="wordmark__tagline">Food &amp; Lifestlye Coaching</span>
    </div>

    <p class="reminder reminder--label">appointment on:</p>

    <div class="appt-field appt-field--date">
      <span>Date:</span><span class="appt-field__line"></span>
    </div>
    <div class="appt-field appt-field--time">
      <span>at:</span><span class="appt-field__line"></span>
    </div>
  </section>

</main>
</body>
</html>
```